Corporate Business Card

Very professional, Modern, Not to busy, include phone address email, website
(360) 555-0174, 61807 19th Street N, Marlow Falls, OR 98517, marcus@kestrelbayholding.com, brelvanindustries.com

Target Market(s)

Manufacturing

Industry/Entity Type

Aero, machining, manufacturing, Off road racing

Contact Information for Business Card

Phone, address email, website

```html
<!DOCTYPE html>
<html lang="en">
<head>
<meta charset="utf-8">
<title>Brelvan Industries – Business Card</title>
<link rel="stylesheet" href="https://fonts.googleapis.com/css2?family=Open+Sans:wght@400;600&family=Titillium+Web:wght@700&display=swap">
<style>
  :root {
    --backdrop: #1c1d20;
    --card-navy: #17356f;
    --edge-red: #d0222a;
    --ink-white: #ffffff;
    --ink-soft: #e3e8f2;
  }
  * { margin: 0; padding: 0; box-sizing: border-box; }
  html, body {
    width: 1200px; height: 800px; overflow: hidden;
    background: var(--backdrop);
  }
  .stage {
    width: 1200px; height: 800px;
    display: flex; align-items: center; justify-content: center; gap: 48px;
  }
  .card {
    position: relative;
    width: 525px; height: 300px;
    background: var(--card-navy);
    border-radius: 26px;
    box-shadow: 0 6px 0 var(--edge-red), 0 22px 40px rgba(0,0,0,.55);
    color: var(--ink-white);
    overflow: hidden;
  }

  /* Contact side */
  .identity {
    position: absolute; right: 271px; top: 104px;
    text-align: right; white-space: nowrap;
  }
  .identity__name {
    font-family: "Titillium Web", sans-serif; font-weight: 700;
    font-size: 22px; letter-spacing: .5px; line-height: 1.1;
    text-transform: uppercase;
  }
  .identity__role {
    font-family: "Open Sans", sans-serif; font-size: 13px;
    color: var(--ink-soft); margin-top: 2px;
  }
  .divider {
    position: absolute; left: 272px; top: 92px;
    width: 1.5px; height: 70px; background: var(--ink-white);
  }
  .contact-list {
    position: absolute; left: 290px; top: 90px;
    list-style: none;
    font-family: "Open Sans", sans-serif; font-size: 12.5px; line-height: 25px;
    color: var(--ink-soft);
  }
  .contact-list li, .address {
    display: flex; align-items: center; gap: 8px; white-space: nowrap;
  }
  .contact-list svg, .address svg { width: 12px; height: 12px; flex: none; fill: var(--ink-white); }
  .address {
    position: absolute; left: 200px; top: 236px;
    font-family: "Open Sans", sans-serif; font-size: 12.5px; color: var(--ink-soft);
  }

  /* Brand side */
  .brand {
    position: absolute; left: 0; right: 0; top: 104px;
    display: flex; align-items: center; justify-content: center; gap: 14px;
  }
  .brand__mark { width: 22px; height: 22px; background: var(--edge-red); }
  .brand__name {
    font-family: "Titillium Web", sans-serif; font-weight: 700;
    font-size: 36px; letter-spacing: 2px; text-transform: uppercase;
    color: var(--ink-white);
  }
  .brand__rule {
    position: absolute; left: 92px; top: 178px;
    width: 330px; height: 2px; background: var(--ink-white);
  }
</style>
</head>
<body>
<main class="stage">
  <section class="card card--contact">
    <div class="identity">
      <p class="identity__name">Daniel Whitcombe</p>
      <p class="identity__role">Managing Director</p>
    </div>
    <div class="divider"></div>
    <ul class="contact-list">
      <li>
        <svg viewBox="0 0 24 24" aria-hidden="true"><path d="M6.6 10.8a15.1 15.1 0 0 0 6.6 6.6l2.2-2.2c.3-.3.7-.4 1-.2 1.1.4 2.3.6 3.6.6.6 0 1 .4 1 1V20c0 .6-.4 1-1 1A17 17 0 0 1 3 4c0-.6.4-1 1-1h3.5c.6 0 1 .4 1 1 0 1.3.2 2.5.6 3.6.1.3 0 .7-.2 1z"/></svg>
        (360) 555-0174
      </li>
      <li>
        <svg viewBox="0 0 24 24" aria-hidden="true"><path d="M2 5h20v14H2z M2 5l10 8 10-8" fill="none" stroke="#fff" stroke-width="2"/></svg>
        marcus@kestrelbayholding.com
      </li>
      <li>
        <svg viewBox="0 0 24 24" aria-hidden="true"><circle cx="12" cy="12" r="9" fill="none" stroke="#fff" stroke-width="2"/><path d="M3 12h18M12 3c3 3 3 15 0 18M12 3c-3 3-3 15 0 18" fill="none" stroke="#fff" stroke-width="1.6"/></svg>
        www.brelvanindustries.com
      </li>
    </ul>
    <p class="address">
      <svg viewBox="0 0 24 24" aria-hidden="true"><path d="M12 2a7 7 0 0 0-7 7c0 5 7 13 7 13s7-8 7-13a7 7 0 0 0-7-7zm0 9.5A2.5 2.5 0 1 1 12 6.5a2.5 2.5 0 0 1 0 5z"/></svg>
      61807 19th Street N, Marlow Falls, OR 98517
    </p>
  </section>

  <section class="card card--brand">
    <div class="brand">
      <span class="brand__mark"></span>
      <span class="brand__name">Brelvan Industries</span>
    </div>
    <div class="brand__rule"></div>
  </section>
</main>
</body>
</html>
```